I need a book cover design for my book called Guard Verbanetti Against Civic Fervor. I want it to grab attention. The book cover needs to portray the fact that the ideology of Lucia Verbanetti and Otto Brenn are in conflict. One idea is a drawing of Verbanetti as a child and Brenn facing each other with serious or stern looks on their faces. Or maybe Verbanetti as an adult facing Brenn. Perhaps with a Verbanetti classroom in the background. I am open to ideas. I have uploaded some pictures in case you could use a few or get ideas from them. I have written something for the back of the book, but I will post it here when we get that far.

Target Market(s)

Verbanetti organizations, Verbanetti teachers, parents of Verbanetti students

Industry/Entity Type

Education, politics

Font styles to use
Serif

Colors

Designer to choose colors to be used in the design.

Requirements
Must have
• I want to include a subtitle: Roused Verbanetti Academies are Forsaking the Lessons of Lucia Verbanetti.
Nice to have
• See Project Description

```html
<!DOCTYPE html>
<html lang="en">
<head>
<meta charset="utf-8">
<title>Guard Verbanetti Against Civic Fervor — Book Cover</title>
<link rel="stylesheet" href="https://fonts.googleapis.com/css2?family=Bebas+Neue&family=Marcellus&display=swap">
<style>
  :root {
    --backdrop: #dedede;
    --cover-black: #050505;
    --photo-dark: #1c1c1c;
    --photo-mid: #3a3a3a;
    --gold-light: #e6c96f;
    --gold: #c9a449;
    --gold-deep: #9c7a2a;
    --white: #ffffff;
  }
  * { margin: 0; padding: 0; box-sizing: border-box; }
  html, body {
    width: 1200px;
    height: 1200px;
    overflow: hidden;
    background: var(--backdrop);
  }
  .book-cover {
    position: absolute;
    left: 220px;
    top: 30px;
    width: 760px;
    height: 1140px;
    background: var(--cover-black);
    overflow: hidden;
  }
  .classroom-photo {
    position: absolute;
    left: 0; top: 0;
    width: 100%;
    height: 731px;
    background:
      linear-gradient(180deg, rgba(0,0,0,0.15) 0%, rgba(0,0,0,0.35) 100%),
      radial-gradient(ellipse at 50% 70%, var(--photo-mid) 0%, var(--photo-dark) 75%);
  }
  .title {
    position: absolute;
    left: 0; top: 100px;
    width: 100%;
    text-align: center;
    font-family: "Bebas Neue", "Oswald", sans-serif;
    line-height: 0.86;
  }
  .title span { display: block; }
  .title-gold {
    background: linear-gradient(90deg, var(--gold-light) 0%, var(--gold) 55%, var(--gold-deep) 100%);
    -webkit-background-clip: text;
    background-clip: text;
    color: transparent;
  }
  .title-guard { font-size: 158px; }
  .title-verbanetti { font-size: 156px; letter-spacing: 1px; margin-top: 4px; }
  .title-white { color: var(--white); }
  .title-against { font-size: 90px; margin-top: 30px; }
  .title-fervor { font-size: 94px; margin-top: 8px; }
  .portrait-medallion {
    position: absolute;
    left: 275px;
    top: 626px;
    width: 210px;
    height: 210px;
  }
  .subtitle {
    position: absolute;
    left: 0; top: 886px;
    width: 100%;
    text-align: center;
    font-family: "Marcellus", serif;
    font-size: 31px;
    line-height: 57px;
    letter-spacing: 1.5px;
    color: var(--gold);
  }
  .author-name {
    position: absolute;
    left: 0; top: 1032px;
    width: 100%;
    text-align: center;
    font-family: "Marcellus", serif;
    font-size: 26px;
    letter-spacing: 2px;
    color: var(--white);
  }
</style>
</head>
<body>
  <div class="book-cover">
    <div class="classroom-photo" role="img" aria-label="Black and white photograph of children working on mats in an early Verbanetti classroom"></div>

    <h1 class="title">
      <span class="title-gold title-guard">Guard</span>
      <span class="title-gold title-verbanetti">Verbanetti</span>
      <span class="title-white title-against">Against</span>
      <span class="title-white title-fervor">Civic Fervor</span>
    </h1>

    <svg class="portrait-medallion" viewBox="0 0 210 210" aria-hidden="false">
      <defs>
        <linearGradient id="ring-gold" x1="0" y1="0" x2="1" y2="1">
          <stop offset="0" stop-color="#f3dc8c"/>
          <stop offset="0.45" stop-color="#c9a449"/>
          <stop offset="0.8" stop-color="#8a6521"/>
          <stop offset="1" stop-color="#e2c06a"/>
        </linearGradient>
        <radialGradient id="portrait-tone" cx="0.5" cy="0.45" r="0.6">
          <stop offset="0" stop-color="#8a8a8a"/>
          <stop offset="0.6" stop-color="#3a3a3a"/>
          <stop offset="1" stop-color="#111111"/>
        </radialGradient>
      </defs>
      <circle cx="105" cy="105" r="104" fill="url(#ring-gold)"/>
      <circle cx="105" cy="105" r="92" fill="#1a1a1a"/>
      <circle cx="105" cy="105" r="87" fill="url(#portrait-tone)" role="img" aria-label="Black and white portrait of Lucia Verbanetti"/>
    </svg>

    <p class="subtitle">Roused Verbanetti Academies are Forsaking<br>the Lessons of Lucia Verbanetti</p>
    <p class="author-name">AUTHOR NAME</p>
  </div>
</body>
</html>
```